Spice Business needs a packaging design

Creative Brief Document

Project Name – Spice & Seasoning blends

Project brief summary
- Brief summary of the project
We are excited to launch a new spice company called “Meadow’s Own,” dedicated to providing sustainably sourced, high-quality spices and spice blends. We are currently exploring packaging materials for PET jars and gift bundle boxes.
The visual identity should convey a sense of purity, earthiness, vibrancy, and gourmet appeal, capturing the essence of spices while ensuring a global appeal.

Products

All Purpose Seasoning
Curry Powder
Beef Bouillon
Chicken Bouillon
Garlic & Herb
Jollof Rice
Seasoning Salt

Jar & Lid Details (see attached files)

- Reason behind brand name

“Meadow’s Own” name to communicate pure, natural and REAL product.

- What are your business goals?
To show
1. authenticity of product - Pure & High-quality spices with no additives
2. Eco-consiousness (sustainability)
3. Vibrancy - Naturally rich and flavourful
4. Breath of fresh air
5. Exciting product
6. Premium product, yet accessible
7. Gain consumer confidence around transparency/honesty
8. Gain market share from established competitors, with a strong market leader for many years
9. Global market address

Target audience?

Mass market & Institutions (Hotels, restaurants etc)
Gift boxes for holidays such as Christmas

Brand positioning?
- Price point? Premium?
Accessible

Tone of Voice
- Eg friendly, fun, professional, expert, eco conscious, etc?

Tone to be elegant, vibrant and align with the idea of authenticity (realness), health and sustainability, just as nature intended it to be.

Modern, Classy and appealing to display in shelves despite the variety of kitchen decors
Pure and Fresh
Vibrant & Flavourful

Crisp labels when printed out

Competitors
- main competition?

Coastal Ember https://www.coastalembergroup.example/
Kivu Pantry https://www.kivupantryea.example/our-brands/kivu-pantry
Vital Mo https://www.vitalmo.example/product-category/foods/

- Which brands are already out there doing a similar thing?

I like global brands such as Lorvo, Pellam’s, Van Drossel, Ashgrove Pure Salt etc

- How to stand out?

Attractive packaging

What are your key messages?
- What is the key idea the pack needs to communicate?

Real product (Authentic)
Fresh
Accessible
Beautiful
Easy to use

- Do you have a unique selling point?

100% Natural (No additives or fillers)
Sustainably sourced
Premium quality at an accessible price
Eco-friendly packaging

Packaging
- Preferred packaging structure?

**We are using pet jars to package all our products for now.
We would like a label that goes round the jar and also with a tamper seal that goes over the lid .

See these video:

Apply labels with tamper seals on Valdon Works' TableTRAK label applicator (vidstream.example)

Brand Name: Meadow’s Own with logo

Unique Selling Point/ Tags: ALL Natural, No preservatives, Premium Quality

Product Name: Chicken Seasoning
(Ladha ya Bata)

Product Picture: Stock pics
 Compact jar, more spice – less plastic waste! 🌍
 Heat levels: visual icons for 0-All flavor, No heat, 1- Mild, 2-Medium, 3-Hot
• Scan for delicious recipes: QR code for recipes
• Enjoy on: [list] Chicken, Seafood, xx, etc
• Symbols to add: Recycling, Sustainability, Eco-Friendly (Better for the environment), Low Carbon Footprint, Suitable for Vegetarians, NQAs Mark of Standardization, Product Barcode, Kenyan Flag (Made in Kenya)

Product Details:
• Ingredients: xxx
• Nutritional Facts
 About xx servings per container
 Serving size x tbsp. (x g)
 Calories per serving x
• Allergen Information
• Net wt.: g and oz – Make this section extremely visible

Company Details:

Willowgate Harvest Co. Ltd
P.O. Box 42615, GPO 00300
Nairobi, Kenya
Tel: 07xxxxxxxx
www.willowgateharvest.example

Storage Details:
Store in a cool and dry place

Target Market(s)

Mass market with a global appeal

Industry/Entity Type

Spices and Seasonings

Colors

Designer to choose colors to be used in the design.

Requirements
Must have
• colourful, quick to read at a glance pics and fonts. Minimal details in the front i.e. logo, spice name, heat levels, weight & centre picture
Should not have
• Hard to easily read fonts

```html
<!DOCTYPE html>
<html lang="en">
<head>
<meta charset="utf-8">
<title>Meadow’s Own – Chicken Seasoning Label</title>
<link rel="stylesheet" href="https://fonts.googleapis.com/css2?family=Montserrat:wght@400;500;700&display=swap">
<style>
  :root {
    --page-bg: #e9e9eb;
    --label-black: #0b0b0b;
    --brand-red: #e2262c;
    --spice-orange: #f2a11c;
    --ribbon-white: #fbf8f2;
    --ribbon-stitch: #e79a2a;
    --ink-dark: #1a1a1a;
    --ink-light: #ffffff;
  }
  * { box-sizing: border-box; margin: 0; padding: 0; }
  html, body {
    width: 1200px; height: 1200px; overflow: hidden;
    background: var(--page-bg);
    font-family: "Montserrat", Arial, sans-serif;
  }
  .jar-label {
    position: absolute; left: 280px; top: 100px;
    width: 640px; height: 1000px;
    background: linear-gradient(to bottom, var(--label-black) 0 49%, var(--spice-orange) 49% 100%);
    overflow: hidden;
  }
  .brand-banner {
    position: absolute; left: 70px; top: 140px;
    width: 500px; height: 140px;
    background: var(--brand-red);
    display: flex; align-items: center; justify-content: center;
  }
  .brand-name {
    color: var(--ink-light);
    font-family: "Montserrat", Arial, sans-serif;
    font-weight: 700; font-size: 44px; line-height: 1;
    white-space: nowrap;
  }
  .product-photo {
    position: absolute; left: 140px; top: 350px;
    width: 360px; height: 250px;
  }
  .name-ribbon {
    position: absolute; left: 65px; top: 640px;
    width: 510px; height: 130px;
    background: var(--ribbon-white);
    border-radius: 4px;
    display: flex; flex-direction: column; align-items: center; justify-content: center;
    text-align: center; color: var(--ink-dark);
  }
  .name-ribbon::before {
    content: ""; position: absolute; inset: 9px;
    border: 2px dashed var(--ribbon-stitch); border-radius: 2px;
  }
  .name-ribbon .product-name { font-weight: 700; font-size: 38px; letter-spacing: 0.5px; }
  .name-ribbon .product-local { font-weight: 500; font-size: 30px; margin-top: 4px; }
  .claims {
    position: absolute; left: 0; right: 0; top: 808px;
    text-align: center; color: var(--ink-light);
    font-weight: 500; font-size: 24px; letter-spacing: 0.5px;
  }
  .claims .claim-row {
    display: inline-block; padding-bottom: 4px;
    border-bottom: 2px solid var(--ink-light);
  }
  .claims .claim-row span + span::before { content: "|"; margin: 0 10px; }
  .claims .claim-single { margin-top: 8px; }
  .net-weight {
    position: absolute; left: 0; right: 0; top: 920px;
    text-align: center; color: var(--ink-light);
    font-weight: 500; font-size: 20px;
  }
</style>
</head>
<body>
  <main class="jar-label">
    <div class="brand-banner">
      <span class="brand-name">Meadow’s Own</span>
    </div>

    <svg class="product-photo" viewBox="0 0 360 250" role="img" aria-label="Photo of a wooden bowl heaped with golden chicken seasoning powder">
      <defs>
        <radialGradient id="spiceTone" cx="50%" cy="40%" r="60%">
          <stop offset="0" stop-color="#e6a032"/>
          <stop offset="0.6" stop-color="#c7862f"/>
          <stop offset="1" stop-color="#8e6640"/>
        </radialGradient>
      </defs>
      <ellipse cx="180" cy="125" rx="180" ry="125" fill="url(#spiceTone)"/>
    </svg>

    <div class="name-ribbon">
      <span class="product-name">CHICKEN SEASONING</span>
      <span class="product-local">(LADHA YA BATA)</span>
    </div>

    <div class="claims">
      <div class="claim-row"><span>ALL NATURAL</span><span>PREMIUM QUALITY</span></div>
      <div class="claim-single">NO PRESERVATIVES</div>
    </div>

    <div class="net-weight">NT. WT. 5oz (141gr)</div>
  </main>
</body>
</html>
```